Bookcover: Lessons From the Silent Orchard

I am publishing a super-low-cost innovation book for €4,99 on Bravolo Self Release to help everyone become a great innovator: young ambitious people without college education nor a big budget. Do you want to help me?

Brief:
Design a book cover 1600 x 2560 pixels for BSR.
Main title: Lessons From the Silent Orchard
Sub title: mindset - insights - skills & tools
Author: Maarten de Klerk
Design: captive, and appealing to everyone
Target Group: young ambitious people without college education

For bravolo please format the height/width ratio of 1.6:1

```html
<!DOCTYPE html>
<html lang="en">
<head>
<meta charset="utf-8">
<title>Lessons From the Silent Orchard — Book Cover</title>
<link href="https://fonts.googleapis.com/css2?family=Oswald:wght@400;500;600&display=swap" rel="stylesheet">
<style>
  :root {
    --backdrop: #e38b3c;
    --navy: #16304b;
    --orange: #e58a35;
    --orange-muted: #c9783a;
    --white: #ffffff;
  }
  html, body {
    margin: 0;
    padding: 0;
    width: 1200px;
    height: 1200px;
    overflow: hidden;
    background: var(--backdrop);
    font-family: "Oswald", "Arial Narrow", sans-serif;
  }
  .cover {
    position: absolute;
    left: 252px;
    top: 68px;
    width: 695px;
    height: 1063px;
    background: var(--navy);
    overflow: hidden;
  }
  .author {
    position: absolute;
    left: 0;
    top: 36px;
    width: 100%;
    text-align: center;
    color: var(--white);
    font-weight: 500;
    font-size: 62px;
    line-height: 80px;
    letter-spacing: 1px;
    margin: 0;
  }
  .frame-lines {
    position: absolute;
    left: 0;
    top: 0;
    width: 695px;
    height: 1063px;
  }
  .icon-slot {
    position: absolute;
    background: var(--orange-muted);
    border-radius: 6px;
  }
  .icon-slot.round { border-radius: 50%; }
  .title {
    margin: 0;
    font-weight: 500;
    text-transform: uppercase;
  }
  .title-line {
    position: absolute;
    display: flex;
    align-items: center;
    justify-content: center;
    box-sizing: border-box;
    color: var(--white);
    line-height: 1;
  }
  .title-line.boxed {
    left: 146px;
    width: 375px;
    height: 136px;
    border: 3px solid var(--orange);
    background: var(--navy);
    font-size: 92px;
  }
  .title-line.band {
    left: 146px;
    top: 483px;
    width: 404px;
    height: 135px;
    background: var(--orange);
    font-size: 108px;
  }
  .title-line.large {
    left: 20px;
    top: 630px;
    width: 655px;
    height: 150px;
    font-size: 162px;
  }
  .subtitle {
    position: absolute;
    left: 0;
    top: 986px;
    width: 100%;
    text-align: center;
    color: var(--orange);
    font-weight: 500;
    font-size: 30px;
    line-height: 40px;
    letter-spacing: 0.5px;
    margin: 0;
  }
</style>
</head>
<body>
  <main class="cover">
    <p class="author">MAARTEN DE KLERK</p>

    <svg class="frame-lines" viewBox="0 0 695 1063" aria-hidden="true">
      <g stroke="#e58a35" stroke-width="3" fill="#e58a35">
        <line x1="20" y1="146" x2="675" y2="146"/>
        <line x1="20" y1="213" x2="675" y2="213"/>
        <line x1="20" y1="802" x2="675" y2="802"/>
        <line x1="20" y1="984" x2="675" y2="984"/>
        <line x1="20" y1="330" x2="146" y2="330"/>
        <line x1="20" y1="470" x2="146" y2="470"/>
        <line x1="20" y1="580" x2="146" y2="580"/>
        <line x1="20" y1="690" x2="146" y2="690" stroke-opacity="0"/>
        <line x1="550" y1="330" x2="675" y2="330"/>
        <line x1="550" y1="440" x2="675" y2="440"/>
        <line x1="550" y1="545" x2="675" y2="545"/>
        <line x1="146" y1="146" x2="146" y2="213"/>
        <line x1="550" y1="213" x2="550" y2="630"/>
        <line x1="146" y1="213" x2="146" y2="630"/>
        <line x1="225" y1="802" x2="290" y2="984"/>
        <line x1="470" y1="802" x2="405" y2="984"/>
        <circle cx="20" cy="146" r="5"/><circle cx="675" cy="146" r="5"/>
        <circle cx="20" cy="213" r="5"/><circle cx="675" cy="213" r="5"/>
        <circle cx="20" cy="802" r="5"/><circle cx="675" cy="802" r="5"/>
        <circle cx="20" cy="984" r="5"/><circle cx="675" cy="984" r="5"/>
        <circle cx="20" cy="330" r="4"/><circle cx="20" cy="470" r="4"/><circle cx="20" cy="580" r="4"/>
        <circle cx="675" cy="330" r="4"/><circle cx="675" cy="440" r="4"/><circle cx="675" cy="545" r="4"/>
      </g>
    </svg>

    <div class="icon-slot" style="left:160px;top:160px;width:48px;height:46px" role="img" aria-label="Small innovation icon"></div>
    <div class="icon-slot" style="left:225px;top:160px;width:48px;height:46px" role="img" aria-label="Small innovation icon"></div>
    <div class="icon-slot" style="left:290px;top:160px;width:48px;height:46px" role="img" aria-label="Small innovation icon"></div>
    <div class="icon-slot" style="left:355px;top:160px;width:48px;height:46px" role="img" aria-label="Small innovation icon"></div>
    <div class="icon-slot" style="left:420px;top:160px;width:48px;height:46px" role="img" aria-label="Small innovation icon"></div>
    <div class="icon-slot" style="left:485px;top:160px;width:48px;height:46px" role="img" aria-label="Small innovation icon"></div>

    <div class="icon-slot round" style="left:45px;top:228px;width:90px;height:90px" role="img" aria-label="Light bulb illustration"></div>
    <div class="icon-slot" style="left:45px;top:345px;width:90px;height:110px" role="img" aria-label="Idea sketches illustration"></div>
    <div class="icon-slot round" style="left:45px;top:485px;width:80px;height:80px" role="img" aria-label="Circular diagram illustration"></div>
    <div class="icon-slot" style="left:45px;top:595px;width:90px;height:60px" role="img" aria-label="Growth chart illustration"></div>

    <div class="icon-slot round" style="left:565px;top:225px;width:95px;height:95px" role="img" aria-label="Compass illustration"></div>
    <div class="icon-slot round" style="left:565px;top:338px;width:95px;height:90px" role="img" aria-label="Brain illustration"></div>
    <div class="icon-slot" style="left:570px;top:455px;width:85px;height:80px" role="img" aria-label="Flow diagram illustration"></div>
    <div class="icon-slot" style="left:570px;top:560px;width:95px;height:90px" role="img" aria-label="Network map illustration"></div>

    <div class="icon-slot round" style="left:40px;top:840px;width:100px;height:100px" role="img" aria-label="Gear illustration"></div>
    <div class="icon-slot" style="left:150px;top:850px;width:70px;height:110px" role="img" aria-label="City buildings illustration"></div>
    <div class="icon-slot round" style="left:290px;top:830px;width:120px;height:120px" role="img" aria-label="Light bulb illustration"></div>
    <div class="icon-slot" style="left:475px;top:835px;width:80px;height:110px" role="img" aria-label="Connected ideas illustration"></div>
    <div class="icon-slot round" style="left:560px;top:840px;width:110px;height:110px" role="img" aria-label="Globe illustration"></div>

    <h1 class="title">
      <span class="title-line boxed" style="top:212px">LESSONS</span>
      <span class="title-line boxed" style="top:347px">FROM THE</span>
      <span class="title-line band">SILENT</span>
      <span class="title-line large">ORCHARD</span>
    </h1>

    <p class="subtitle">MINDSET - INSIGHTS - SKILLS &amp; TOOLS</p>
  </main>
</body>
</html>
```